Design a styled business card for an intimacy and attachment psychologist

I am a Psychologist providing online therapy to patients across the United States. My work is interpersonal and emotion-focused, with an emphasis on the client-therapist relationship. My primary areas of work are very personal, including sexuality and gender, abuse and trauma, and grief and loss. My target audience will be adults of all ages 18+.
My business card should convey a warm and inviting feeling of professionalism that is also casual and comfortable.
The front should be fairly simple and professional, consisting of:
- My name, Dr. Rosalind Petrakis
- My title, Licensed Psycholigist
- My logo
On either the front or the back, my contact information should be listed:
- ros@drrospetrakis.example
- 555.014.7788
- drrospetrakis.example
On the rear, I would like a description of the areas that I specialize in. This can be formatted in any way that appears stylistically interesting.
Individual and Couples
Relationships and Infidelity
Sexual Health & Aging
Gender Identity & Sexual Orientation
Abuse and Trauma
Sexual Compulsivity & Addiction
Sexual Dysfunction
Target Market(s)
My target audience will be adults of all ages 18+.
Industry/Entity Type
Psychology
Contact Information for Business Card
The front should be fairly simple and professional, consisting of: - My name, Dr. Rosalind Petrakis - My title, Licensed Psycholigist - My logo On either the front or the back, my contact information should be listed: - ros@drrospetrakis.example - 555.014.7788 - drrospetrakis.example On the rear, I would like a description of the areas that I specialize in. This can be formatted in any way that appears stylistically interesting. Individual and Couples Relationships and Infidelity Sexual Health & Aging Gender Identity & Sexual Orientation Abuse and Trauma Sexual Compulsivity & Addiction Sexual Dysfunction
- Follow brand guide

```html
<!DOCTYPE html>
<html lang="en">
<head>
<meta charset="UTF-8">
<title>Dr. Rosalind Petrakis — Business Card</title>
<link rel="stylesheet" href="https://fonts.googleapis.com/css2?family=Lato:ital,wght@0,400;0,700;0,900;1,400&display=swap">
<style>
  :root {
    --backdrop: #2c2c2f;
    --paper: #ffffff;
    --navy: #2a2550;
    --ink: #1f1c3d;
    --muted: #6d6d78;
    --teal: #5bbfa4;
    --orange: #f4a62a;
    --red: #e8434c;
    --mint: #bfe3da;
    --list-text: #f2f1f8;
  }
  * { box-sizing: border-box; margin: 0; padding: 0; }
  html, body { width: 1200px; height: 952px; overflow: hidden; }
  body {
    background: var(--backdrop);
    font-family: "Lato", sans-serif;
    position: relative;
  }
  .card {
    position: absolute;
    width: 560px;
    height: 320px;
    border-radius: 22px;
    box-shadow: 0 14px 30px rgba(0,0,0,.45);
  }
  .card--front { left: 590px; top: 100px; background: var(--paper); }
  .card--back { left: 60px; top: 520px; background: var(--navy); }

  /* Front */
  .brand {
    position: absolute; left: 36px; top: 112px;
    display: flex; align-items: center; gap: 14px;
  }
  .brand__dot {
    width: 58px; height: 58px; border-radius: 50%;
    background: var(--mint); border: 4px solid var(--ink);
    flex: none;
  }
  .brand__name {
    font-weight: 700; font-size: 22px; line-height: 1.1;
    color: var(--ink); width: 130px;
  }
  .details { position: absolute; left: 260px; top: 96px; }
  .details__name {
    font-weight: 900; font-size: 19px; letter-spacing: .06em;
    color: var(--ink); text-transform: uppercase;
  }
  .details__title {
    font-style: italic; font-size: 14px; color: var(--muted); margin-top: 4px;
  }
  .details__rule { width: 48px; height: 2px; background: var(--ink); margin: 10px 0 12px; }
  .contact { list-style: none; }
  .contact li {
    display: flex; align-items: center; gap: 8px;
    font-size: 13.5px; color: var(--muted); margin-bottom: 7px;
  }
  .contact__icon {
    width: 18px; height: 18px; border-radius: 3px;
    display: flex; align-items: center; justify-content: center;
  }
  .contact__icon--phone { background: var(--teal); }
  .contact__icon--mail { background: var(--orange); }
  .contact__icon--web { background: var(--red); }

  /* Back */
  .specialties { position: absolute; left: 34px; top: 34px; list-style: none; }
  .specialties li {
    display: flex; align-items: center; gap: 8px;
    color: var(--list-text); font-size: 16px; margin-bottom: 7px;
  }
  .tick { width: 14px; height: 14px; background: #fff; border-radius: 2px; flex: none; }
  .back-brand {
    position: absolute; right: 36px; bottom: 36px;
    display: flex; align-items: center; gap: 12px;
  }
  .back-brand__dot {
    width: 96px; height: 96px; border-radius: 50%;
    background: var(--mint); border: 5px solid #fff;
  }
  .back-brand__name {
    color: var(--list-text); font-weight: 700; font-size: 17px; width: 110px; line-height: 1.15;
  }
</style>
</head>
<body>
  <section class="card card--front" aria-label="Card front">
    <div class="brand">
      <span class="brand__dot"></span>
      <span class="brand__name">Dr. Rosalind Petrakis</span>
    </div>
    <div class="details">
      <h1 class="details__name">Dr. Rosalind Petrakis</h1>
      <p class="details__title">Licensed Psycholigist</p>
      <div class="details__rule"></div>
      <ul class="contact">
        <li><span class="contact__icon contact__icon--phone">
          <svg width="11" height="11" viewBox="0 0 24 24"><path fill="#fff" d="M6.6 10.8a15 15 0 0 0 6.6 6.6l2.2-2.2c.3-.3.7-.4 1-.2 1.1.4 2.3.6 3.6.6.6 0 1 .4 1 1V20c0 .6-.4 1-1 1A17 17 0 0 1 3 4c0-.6.4-1 1-1h3.5c.6 0 1 .4 1 1 0 1.3.2 2.5.6 3.6.1.3 0 .7-.2 1z"/></svg>
        </span>555.014.7788</li>
        <li><span class="contact__icon contact__icon--mail">
          <svg width="12" height="10" viewBox="0 0 24 18"><rect x="1" y="1" width="22" height="16" fill="none" stroke="#fff" stroke-width="2"/><path d="M1 1l11 9 11-9" fill="none" stroke="#fff" stroke-width="2"/></svg>
        </span>ros@drrospetrakis.example</li>
        <li><span class="contact__icon contact__icon--web">
          <svg width="12" height="12" viewBox="0 0 24 24" fill="none" stroke="#fff" stroke-width="2"><circle cx="12" cy="12" r="10"/><path d="M2 12h20M12 2c3 3 3 17 0 20M12 2c-3 3-3 17 0 20"/></svg>
        </span>drrospetrakis.example</li>
      </ul>
    </div>
  </section>

  <section class="card card--back" aria-label="Card back">
    <ul class="specialties">
      <li><span class="tick"><svg width="14" height="14" viewBox="0 0 14 14"><path d="M3 7l3 3 6-7" fill="none" stroke="#e8434c" stroke-width="2"/></svg></span>Stylistically Interesting.</li>
      <li><span class="tick"><svg width="14" height="14" viewBox="0 0 14 14"><path d="M3 7l3 3 6-7" fill="none" stroke="#e8434c" stroke-width="2"/></svg></span>Individual And Couples</li>
      <li><span class="tick"><svg width="14" height="14" viewBox="0 0 14 14"><path d="M3 7l3 3 6-7" fill="none" stroke="#e8434c" stroke-width="2"/></svg></span>Relationships And Infidelity</li>
      <li><span class="tick"><svg width="14" height="14" viewBox="0 0 14 14"><path d="M3 7l3 3 6-7" fill="none" stroke="#e8434c" stroke-width="2"/></svg></span>Sexual Health &amp; Aging</li>
      <li><span class="tick"><svg width="14" height="14" viewBox="0 0 14 14"><path d="M3 7l3 3 6-7" fill="none" stroke="#e8434c" stroke-width="2"/></svg></span>Gender Identity &amp; Sexual Orientation</li>
      <li><span class="tick"><svg width="14" height="14" viewBox="0 0 14 14"><path d="M3 7l3 3 6-7" fill="none" stroke="#e8434c" stroke-width="2"/></svg></span>Abuse And Trauma</li>
      <li><span class="tick"><svg width="14" height="14" viewBox="0 0 14 14"><path d="M3 7l3 3 6-7" fill="none" stroke="#e8434c" stroke-width="2"/></svg></span>Sexual Compulsivity &amp; Addiction</li>
      <li><span class="tick"><svg width="14" height="14" viewBox="0 0 14 14"><path d="M3 7l3 3 6-7" fill="none" stroke="#e8434c" stroke-width="2"/></svg></span>Sexual Dysfunction</li>
    </ul>
    <div class="back-brand">
      <span class="back-brand__name">Dr. Rosalind Petrakis</span>
      <span class="back-brand__dot"></span>
    </div>
  </section>
</body>
</html>
```